Bright Path Therapies business cards and stationary

Need business cards and stationary designed to match previously made logo for for a new company based in Sydney NSW called 'Bright Path Therapies'.

We provide early intervention services and diagnostic assessment for children with disability and their families. I would like designs that are colourful and child friendly - possibly using feet/footprints/steps on a white background. The final design should communicate that we are family friendly, accepting and fun to work with.

Target Market(s)

Parents and Families
Teachers
Allied Health Professionals

Industry/Entity Type

Psychology

Contact Information for Business Card

Bright Path Therapies
www.brightpaththerapies.example
info@brightpaththerapies.example

Font styles to use
Sans Serif
Decorative
Script

Requirements
Must have
• Match the font and colour scheme of logo, along with footprint picture
Nice to have
• Clean and simple, while reflecting that I am working with families.
• Also- editable for when we make staff specific cards.

```html
<!DOCTYPE html>
<html lang="en">
<head>
<meta charset="utf-8">
<title>Bright Path Therapies – Business Card</title>
<link href="https://fonts.googleapis.com/css2?family=Source+Sans+3:ital,wght@0,400;0,600;0,700;1,400&display=swap" rel="stylesheet">
<style>
  :root {
    --backdrop: #e6e4e1;
    --card: #121212;
    --card-edge: #1c1c1c;
    --silver: #9a9a9a;
    --tagline: #8c8c8c;
    --coral: #ef4438;
    --blue: #2f8fd8;
    --white: #f2f2f2;
  }
  * { margin: 0; padding: 0; box-sizing: border-box; }
  html, body {
    width: 1200px; height: 864px; overflow: hidden;
    background: var(--backdrop);
    font-family: "Source Sans 3", Arial, sans-serif;
  }
  .stage { position: relative; width: 1200px; height: 864px; }
  .card {
    position: absolute;
    width: 540px; height: 309px;
    background: linear-gradient(160deg, var(--card-edge), var(--card));
    border-radius: 4px;
    box-shadow: 0 10px 28px rgba(0,0,0,.28);
    overflow: hidden;
  }
  .card-front { left: 70px; top: 120px; }
  .card-back { left: 590px; top: 430px; }

  /* front */
  .brand {
    position: absolute; left: 60px; top: 78px;
    display: flex; align-items: center; gap: 18px;
  }
  .brand-dot {
    width: 64px; height: 64px; border-radius: 50%;
    background: var(--silver);
  }
  .brand-name {
    color: var(--silver);
    font-size: 34px; font-weight: 600; letter-spacing: .5px; line-height: 1;
  }
  .tagline {
    position: absolute; left: 60px; top: 190px; width: 400px;
    color: var(--tagline);
    font-style: italic; font-size: 15px; line-height: 1.35;
  }

  /* back */
  .mark {
    position: absolute; left: 48px; top: 70px; width: 150px;
    display: flex; flex-direction: column; align-items: center; gap: 12px;
  }
  .mark-circle {
    width: 138px; height: 138px; border-radius: 50%;
    background: var(--coral);
  }
  .mark-name {
    color: var(--coral); font-size: 13px; font-weight: 600; white-space: nowrap;
  }
  .divider {
    position: absolute; left: 232px; top: 40px; width: 1px; height: 230px;
    background: linear-gradient(to bottom, transparent, #8a8a8a 40%, #8a8a8a 60%, transparent);
  }
  .contact {
    position: absolute; left: 256px; top: 58px;
    color: var(--white); font-size: 15.5px; line-height: 1.3;
  }
  .person-name { color: var(--coral); font-weight: 700; text-transform: uppercase; font-size: 16px; }
  .person-role { color: var(--blue); font-weight: 600; text-transform: uppercase; font-size: 16px; margin-bottom: 2px; }
  .contact-row { display: flex; align-items: center; gap: 8px; }
  .contact-row svg { width: 13px; height: 13px; fill: var(--coral); flex: none; }
  .address { margin-bottom: 2px; }
</style>
</head>
<body>
<main class="stage">

  <section class="card card-front">
    <div class="brand">
      <span class="brand-dot"></span>
      <span class="brand-name">Bright Path Therapies</span>
    </div>
    <p class="tagline">Early intervention services &amp; diagnostic assessment for children with disability and their families.</p>
  </section>

  <section class="card card-back">
    <div class="mark">
      <span class="mark-circle"></span>
      <span class="mark-name">Bright Path Therapies</span>
    </div>
    <span class="divider"></span>
    <div class="contact">
      <div class="person-name">Alex Morgan</div>
      <div class="person-role">CEO/Founder</div>
      <div class="address">42 Wattle Grove Road<br>Parramatta, NSW 2150</div>
      <div class="contact-row">
        <svg viewBox="0 0 16 16" aria-hidden="true"><path d="M3 1h3l1.5 4-2 1.3a9 9 0 0 0 4.2 4.2L11 8.5l4 1.5v3a2 2 0 0 1-2 2A12 12 0 0 1 1 3a2 2 0 0 1 2-2z"/></svg>
        <span>02 5550 1432</span>
      </div>
      <div class="contact-row">
        <svg viewBox="0 0 16 16" aria-hidden="true"><path d="M4 0h8a1 1 0 0 1 1 1v14a1 1 0 0 1-1 1H4a1 1 0 0 1-1-1V1a1 1 0 0 1 1-1zm1 2v10h6V2zm3 11a1 1 0 1 0 0 2 1 1 0 0 0 0-2z"/></svg>
        <span>0491 570 118</span>
      </div>
      <div class="contact-row">
        <svg viewBox="0 0 16 16" aria-hidden="true"><path d="M4 1h7v4H4zM1 6h14v7h-3v2H4v-2H1zm4 5v3h6v-3z"/></svg>
        <span>02 5550 1433</span>
      </div>
      <div class="contact-row">
        <svg viewBox="0 0 16 16" aria-hidden="true"><path d="M1 3h14v10H1zm1.5 1.2v.5L8 8.5l5.5-3.8v-.5z"/></svg>
        <span>info@brightpaththerapies.example</span>
      </div>
      <div class="contact-row">
        <svg viewBox="0 0 16 16" aria-hidden="true"><circle cx="8" cy="8" r="7"/></svg>
        <span>www.brightpaththerapies.example</span>
      </div>
    </div>
  </section>

</main>
</body>
</html>
```